Spiritual Support flyer design

I offer a range of spiritual support options from a drop in group to meditation. I work alone in two locations, one at home and the other in the local town centre therapy centre. I do not want people to be confused about where to go for each item so thought one side could be the town centre group and the other side of the leaflet could be the things I offer from home. I need to find a way to present a list of things I do and make it look inviting so people want to contact me. I want it to feel inspirational, uplifting, light hearted, with a gentle feel of support or coming home to somewhere safe. The leaflet needs to look eye catching as it will be where there are many other leaflets the same size (A5). I love purples, as they tend to be spiritual colours or the look below of light bursting through the clouds seems appropriate picture wise. I do not have a logo.
The title can be Amber Lantern. On one side I would like to introduce a Spiritual Experiences drop-in group held at the Pebble Hall Centre, Colchester 1-2pm every four weeks to share spiritual experiences with others. I can give you more words for that when you are ready. The other side needs to feature the things I offer from my own home which are: Spiritual Counselling, Private email guidance, Meditation one to one, and Amber Lantern Days, which are like a days retreat. It might be a good idea to mention prices but not in an obvious way, so have that just readable in small print.

```html
<!DOCTYPE html>
<html lang="en">
<head>
<meta charset="utf-8">
<title>Amber Lantern – Spiritual Support Flyer</title>
<link rel="stylesheet" href="https://fonts.googleapis.com/css2?family=Cinzel:wght@700&family=Source+Sans+3:wght@300;400;600;700&display=swap">
<style>
  :root {
    --stage: #ececec;
    --paper: #dcdcdd;
    --purple: #6b2fa3;
    --purple-deep: #3a1466;
    --ink-grey: #3f3f44;
    --silver: #f4f4f6;
    --sans: "Source Sans 3", "Myriad Pro", Arial, sans-serif;
    --serif: "Cinzel", "Trajan Pro", Georgia, serif;
  }
  * { box-sizing: border-box; margin: 0; padding: 0; }
  html, body { width: 1200px; height: 841px; overflow: hidden; }
  body { background: var(--stage); font-family: var(--sans); color: var(--purple); position: relative; }

  .flyer { position: absolute; background: var(--paper); box-shadow: 0 2px 6px rgba(0,0,0,.18); overflow: hidden; }
  .flyer--group { left: 82px; top: 40px; width: 504px; height: 715px; }
  .flyer--home  { left: 615px; top: 40px; width: 503px; height: 712px; }

  .frame { position: absolute; border: 2px solid var(--purple); z-index: 3; pointer-events: none; }
  .flyer--group .frame { left: 20px; top: 22px; width: 464px; height: 674px; }
  .flyer--home .frame  { left: 21px; top: 22px; width: 464px; height: 675px; }

  .cosmos {
    position: absolute; left: 0; width: 100%;
    background:
      radial-gradient(ellipse at 30% 45%, rgba(214,120,230,.55), transparent 55%),
      radial-gradient(ellipse at 75% 60%, rgba(120,70,200,.6), transparent 60%),
      linear-gradient(160deg, #2a0d52 0%, #5b2391 45%, #3b1570 75%, #1d0940 100%);
  }
  .flyer--group .cosmos { top: 250px; height: 200px; }
  .flyer--home .cosmos  { top: 0; height: 115px; }

  .band-title {
    position: absolute; left: 0; width: 100%; text-align: center; z-index: 2;
    font-family: var(--serif); font-weight: 700; color: var(--silver);
    text-shadow: 0 2px 3px rgba(0,0,0,.55);
  }
  .band-title--main { top: 292px; font-size: 53px; line-height: 58px; letter-spacing: 1px; }
  .band-title--brand { top: 46px; font-size: 38px; letter-spacing: 1px; }

  .venue { position: absolute; left: 43px; top: 38px; font-size: 18px; line-height: 20px; }
  .contribution { position: absolute; right: 47px; top: 38px; text-align: right; font-weight: 600; font-size: 18px; line-height: 20px; }
  .contribution strong { display: block; font-size: 25px; line-height: 30px; }

  .intro { position: absolute; left: 45px; top: 112px; width: 414px; font-size: 13.4px; line-height: 14.5px; text-align: justify; }
  .intro p + p { margin-top: 14px; }
  .intro b { font-weight: 700; }

  .host { position: absolute; left: 45px; width: 414px; font-size: 15px; line-height: 15.5px; font-weight: 300; text-align: justify; }
  .host b { font-weight: 600; }
  .host--lead { top: 472px; }
  .host--second { top: 598px; }
  .host-contact { position: absolute; left: 45px; top: 536px; }
  .host-contact .email { font-weight: 600; font-size: 15px; }
  .host-contact .phone { color: var(--ink-grey); font-size: 19px; line-height: 22px; margin-top: 2px; }

  .address { position: absolute; left: 0; width: 100%; top: 138px; text-align: center; font-weight: 700; font-size: 20px; line-height: 22px; }

  .service { position: absolute; width: 200px; font-size: 15.5px; line-height: 17px; }
  .service h3 { font-size: 15.5px; font-weight: 700; position: relative; }
  .service h3::before { content: "•"; position: absolute; left: -10px; }
  .service p { font-size: 15px; }
  .service--small p { font-size: 12.6px; line-height: 14.5px; }
  .service b { font-weight: 700; }
  .svc-counselling { left: 54px; top: 234px; }
  .svc-email { left: 252px; top: 232px; }
  .svc-meditation { left: 54px; top: 321px; }
  .svc-day { left: 252px; top: 321px; }

  .booking { position: absolute; top: 424px; font-size: 15px; line-height: 22px; }
  .booking b { font-weight: 600; display: block; }
  .booking--web { left: 56px; }
  .booking--mail { left: 257px; }

  .phone-line { position: absolute; left: 0; width: 100%; top: 483px; text-align: center; font-size: 15px; }
  .phone-line strong { display: block; font-size: 32px; font-weight: 700; line-height: 36px; margin-top: 1px; }

  .photo {
    position: absolute; left: 0; top: 553px; width: 100%; height: 159px;
    background: linear-gradient(90deg, #5a5e66 0%, #9aa0a8 35%, #e7e9ec 60%, #cfd2d6 100%);
  }
</style>
</head>
<body>

<section class="flyer flyer--group" aria-label="Spiritual Experiences drop-in group">
  <div class="frame"></div>
  <p class="venue">A drop-in group at<br>The Pebble Hall Centre,<br>7 Willow Lane, Colchester</p>
  <p class="contribution">Contribution<strong>£5</strong></p>
  <div class="intro">
    <p><b>Mara and Nell</b> invite you to drop in and share any spiritual experiences you may have had, enlightened moments, or developing spiritual gifts, in a supportive environment.</p>
    <p>Perhaps you feel that you are the only one experiencing what you do and would like to talk about it, or listen to others experiences. In the group you can share with like-minded souls for personal development and inspiration.</p>
  </div>
  <div class="cosmos" role="img" aria-label="Purple starry night sky"></div>
  <h1 class="band-title band-title--main">SPIRITUAL<br>EXPERIENCES</h1>
  <p class="host host--lead"><b>Mara Quill</b> – has loved all things spiritual from an early age and provides email consultations, spiritual counselling, and amber lantern days</p>
  <div class="host-contact">
    <p class="email">mara.quill@lanternmail.com</p>
    <p class="phone">01632 960418</p>
  </div>
  <p class="host host--second"><b>Nell Ardent</b> – had a spiritual awakening and became open to angels, is sensitive to energies, and has been on a pathway of self-discovery ever since. She enjoys emotionally supporting others on their life journey.<br>Please contact Mara for future dates.</p>
</section>

<section class="flyer flyer--home" aria-label="Amber Lantern home services">
  <div class="cosmos" role="img" aria-label="Purple starry night sky"></div>
  <div class="frame"></div>
  <h2 class="band-title band-title--brand">AMBER LANTERN</h2>
  <p class="address">@ The Meditation Room,<br>14 Heron Mews,<br>Colchester CO4 9XQ</p>

  <div class="service service--small svc-counselling">
    <h3>Spiritual Counselling</h3>
    <p>Up to an hours confidential one to one support and assistance <b>£45</b></p>
  </div>
  <div class="service svc-email">
    <h3>Private email guidance</h3>
    <p>Response within 24 hours or sooner <b>£45</b></p>
  </div>
  <div class="service svc-meditation">
    <h3>Meditation one to one</h3>
    <p>Bigger or advanced assistance to develop your practice <b>£45</b></p>
  </div>
  <div class="service svc-day">
    <h3>Amber Lantern day</h3>
    <p>A day learning to re-align with your inner being <b>£90</b></p>
  </div>

  <p class="booking booking--web">Please book on line at<b>www.maraquill.co.uk</b></p>
  <p class="booking booking--mail">Or email<b>mara.quill@lanternmail.com</b></p>
  <p class="phone-line">Or telephone<strong>01632 960418</strong></p>

  <div class="photo" role="img" aria-label="Photo of a counsellor in conversation with a client in an office"></div>
</section>

</body>
</html>
```